VitaLedger Plus Trifold

We need a brochure to target retail consumers in the United States. Customers can save a lot of money by using our services and buying medicines through our network. This program is only good for people who are either have no health insurance or are underinsured; which could mean medicaid and donut hole medicare part D customers. I have uploaded our existing flyer. But we want to change it and make it more aspiration. Everyone wants to save money but what do we save money for? So we need good tag line and design that will get people to have a look at the flyer and take action and call the toll free number.
Updates

Paper size should be a normal trifold paper. So it should be able to fold a 81/2 X 11 paper horizontally into a triflod. 

Target Market(s)

Uninsured or underinsured customers aged between 40-80.

Requirements
Must have
• It must be a tri fold which can be put in a leaflet stand at the doctor''s offices.
Nice to have
• We already have money that we are showing. It should have an image with a caption that makes the customer want to pick up and read it. For example, if a TV is at the front then there should be something about how u save money to buy this TV. It should drive the customer to pick up the trifold and  read it as he/she wants to buy this new HDTV but does not have the money and then the flyer explains how they can save money. Please do not repeat the money/cash on the front as we already have that. Please also feel free to change the words to fit the design.

```html
<!DOCTYPE html>
<html lang="en">
<head>
<meta charset="utf-8">
<title>VitaLedger Plus Trifold</title>
<link rel="stylesheet" href="https://fonts.googleapis.com/css2?family=Arimo:wght@400;700&family=Oswald:wght@500;600;700&display=swap">
<style>
  :root {
    --panel-blue-top: #3ba3da;
    --panel-blue-bottom: #1d5c9c;
    --deep-blue: #134d8f;
    --mid-blue: #2386c8;
    --sun-yellow: #e9b523;
    --lemon: #f4e81c;
    --leaf-green: #3c9a3a;
    --call-green: #2f7d2e;
    --soft-white: #e4edf4;
    --ink: #111111;
    --paper: #ffffff;
  }
  * { margin: 0; padding: 0; box-sizing: border-box; }
  html, body { width: 1200px; height: 930px; overflow: hidden; background: var(--paper); }
  .sheet { position: relative; width: 1200px; height: 930px; font-family: "Arimo", Arial, sans-serif; }
  .backdrop { position: absolute; inset: 0; }

  .inside-panel { position: absolute; left: 0; top: 0; width: 405px; height: 930px; color: var(--soft-white); padding: 27px 0 0 15px; }
  .intro { font-size: 16.5px; line-height: 23px; }
  .intro-gap { margin-top: 23px; }
  .benefit { position: absolute; left: 15px; width: 380px; }
  .benefit h3 { font-size: 18px; font-weight: 700; margin-bottom: 7px; }
  .benefit p { font-size: 16.5px; line-height: 26px; padding-left: 15px; }
  .inside-call { position: absolute; left: 0; width: 405px; top: 798px; text-align: center; font-weight: 700; font-size: 22.5px; line-height: 27px; }

  .story-panel { position: absolute; left: 405px; width: 397px; top: 0; height: 800px; }
  .dream-photo { position: absolute; left: 30px; top: 48px; width: 337px; height: 290px; border-radius: 8px; }
  .dream-caption { position: absolute; left: 30px; width: 337px; top: 352px; font-size: 15px; line-height: 21px; color: #3a4652; font-style: normal; text-align: center; }
  .tagline { position: absolute; left: 20px; width: 357px; top: 430px; text-align: center; font-family: "Oswald", "Arial Narrow", sans-serif; font-weight: 600; text-transform: uppercase; color: var(--deep-blue); font-size: 30px; line-height: 38px; }
  .tagline .accent { color: var(--call-green); }
  .back-panel { position: absolute; left: 405px; width: 397px; top: 643px; text-align: center; }
  .brand-name { font-family: "Arimo", Arial, sans-serif; font-weight: 700; color: var(--ink); letter-spacing: 1px; }
  .back-panel .brand-name { font-size: 28px; }
  .back-contact { font-size: 13px; line-height: 21px; color: var(--ink); margin-top: 8px; }

  .money-visual { position: absolute; left: 858px; top: 96px; width: 318px; height: 280px; }
  .headline { position: absolute; left: 802px; width: 398px; top: 410px; text-align: center; font-family: "Oswald", "Arial Narrow", sans-serif; font-weight: 700; text-transform: uppercase; }
  .headline .line { display: block; color: var(--soft-white); font-size: 33px; line-height: 49px; }
  .headline .line.bright { color: #ffffff; }
  .headline .punch { display: block; color: var(--lemon); font-size: 60px; line-height: 62px; }
  .cover-brand { position: absolute; left: 802px; width: 398px; top: 730px; text-align: center; }
  .cover-brand .brand-name { font-size: 35px; }
  .cover-call { position: absolute; left: 802px; width: 398px; top: 826px; text-align: center; font-family: "Oswald", "Arial Narrow", sans-serif; }
  .cover-call .label { color: var(--call-green); font-size: 27px; font-weight: 600; line-height: 32px; }
  .cover-call .number { color: var(--ink); font-size: 39px; font-weight: 600; line-height: 50px; }
</style>
</head>
<body>
<main class="sheet">
  <svg class="backdrop" width="1200" height="930" viewBox="0 0 1200 930" aria-hidden="true">
    <defs>
      <linearGradient id="insideBlue" x1="0" y1="0" x2="0" y2="1">
        <stop offset="0" stop-color="var(--panel-blue-top)"/>
        <stop offset="1" stop-color="var(--panel-blue-bottom)"/>
      </linearGradient>
      <linearGradient id="coverBlue" x1="0" y1="0" x2="0" y2="1">
        <stop offset="0" stop-color="#2e9ad6"/>
        <stop offset="1" stop-color="#1a63a8"/>
      </linearGradient>
      <linearGradient id="swooshGold" x1="0" y1="0" x2="1" y2="0">
        <stop offset="0" stop-color="var(--sun-yellow)"/>
        <stop offset="1" stop-color="var(--lemon)"/>
      </linearGradient>
    </defs>
    <rect x="0" y="0" width="405" height="930" fill="url(#insideBlue)"/>
    <path d="M405 800 C520 820 640 850 802 850 L802 930 L405 930 Z" fill="var(--deep-blue)"/>
    <path d="M405 815 C520 850 650 870 802 860 L802 930 L405 930 Z" fill="var(--mid-blue)"/>
    <path d="M405 850 C540 880 680 880 802 862 L802 930 L405 930 Z" fill="url(#swooshGold)"/>
    <path d="M405 895 C560 905 700 900 802 885 L802 930 L405 930 Z" fill="var(--leaf-green)"/>
    <rect x="802" y="0" width="398" height="930" fill="var(--paper)"/>
    <path d="M802 0 L1200 0 L1200 600 C1100 520 960 700 802 740 Z" fill="var(--deep-blue)"/>
    <path d="M802 0 L1200 0 L1200 560 C1090 500 950 670 802 700 Z" fill="url(#coverBlue)"/>
    <path d="M802 0 L1200 0 L1200 30 C1060 40 940 110 802 160 Z" fill="var(--sun-yellow)"/>
    <line x1="802" y1="0" x2="802" y2="930" stroke="#dfe7ee" stroke-width="1"/>
  </svg>

  <section class="inside-panel">
    <p class="intro">Imagine saving over $1,000 or more on your<br>prescription medications . . .<br>Well Now You Can!</p>
    <p class="intro intro-gap">Start Saving Today!<br>Save more for what matters most.</p>

    <div class="benefit" style="top:205px">
      <h3>VitaLedger Plus</h3>
      <p>Delivers brand name prescription<br>medications directly to your home</p>
    </div>
    <div class="benefit" style="top:305px">
      <h3>VitaLedger Plus</h3>
      <p>Offers the world’s best prices on<br>your medications. Hundreds of medications<br>are available and in-stock today for immedi-<br>ate delivery to your home</p>
    </div>
    <div class="benefit" style="top:474px">
      <h3>VitaLedger Plus</h3>
      <p>Provides the same quality, brand<br>name medications as your local pharmacy,<br>but at lower prices without markup</p>
    </div>
    <div class="benefit" style="top:627px">
      <h3>VitaLedger Plus</h3>
      <p>Is suggested by healthcare<br>professionals as an alternative, cost effective<br>choice for purchasing brand name medica-<br>tions</p>
    </div>

    <p class="inside-call">Call Toll Free<br>1-888-555-0142<br>Start Saving Today!</p>
  </section>

  <section class="story-panel">
    <svg class="dream-photo" viewBox="0 0 337 290" role="img" aria-label="Photo of grandparents on a beach vacation with their grandchildren">
      <defs>
        <linearGradient id="dreamTone" x1="0" y1="0" x2="0" y2="1">
          <stop offset="0" stop-color="#8fcbee"/>
          <stop offset="0.6" stop-color="#5fa9d8"/>
          <stop offset="1" stop-color="#e8d7a6"/>
        </linearGradient>
      </defs>
      <rect x="0" y="0" width="337" height="290" rx="8" fill="url(#dreamTone)"/>
    </svg>
    <p class="dream-caption">That family beach trip you keep putting off?<br>What you save on medicine can get you there.</p>
    <h2 class="tagline">Save on your prescriptions.<br><span class="accent">Spend on your life.</span></h2>
  </section>

  <section class="back-panel">
    <div class="brand-name">VITALEDGER PLUS</div>
    <p class="back-contact">support@vitaledgerplus.com<br>1-888-555-0142</p>
  </section>

  <section class="cover">
    <svg class="money-visual" viewBox="0 0 318 280" role="img" aria-label="Photo of stacked bundles of hundred-dollar bills">
      <defs>
        <linearGradient id="cashTone" x1="0" y1="0" x2="1" y2="1">
          <stop offset="0" stop-color="#e3e8dc"/>
          <stop offset="1" stop-color="#9fae98"/>
        </linearGradient>
      </defs>
      <rect x="0" y="0" width="318" height="280" rx="10" fill="url(#cashTone)" opacity="0.9"/>
    </svg>

    <h1 class="headline">
      <span class="line">Stop paying high</span>
      <span class="line">prices for your</span>
      <span class="line bright">prescription</span>
      <span class="punch">Medications!</span>
    </h1>

    <div class="cover-brand"><div class="brand-name">VITALEDGER PLUS</div></div>

    <div class="cover-call">
      <div class="label">CALL TOLL FREE</div>
      <div class="number">1-888-555-0142</div>
    </div>
  </section>
</main>
</body>
</html>
```